Redesign current business card for food company

i would like to redesign my business card. our company is food company, our product range from chips, juices, milk and etc (mostly dried food stuff).
I want o keep same logo but , the rest is open to new design.
you can check at our website about our company www.torvikeats.com

Target Market(s)

most of food company

Industry/Entity Type

Business

Contact Information for Business Card

I want to keep more to blue color...

Colors
3176b5
abd036

Requirements
Must have
• our old logo
Nice to have
• we do not mind to have nice material on bus card in order to accomplish nice design. for example: using spot uv, embossed and etc.

```html
<!DOCTYPE html>
<html lang="en">
<head>
<meta charset="utf-8">
<title>Torvik Business Card</title>
<link rel="stylesheet" href="https://fonts.googleapis.com/css2?family=Open+Sans:wght@400&display=swap">
<style>
  :root {
    --brand-blue: #3176b5;
    --brand-green: #abd036;
    --card-white: #ffffff;
    --backdrop: #e4e5e7;
    --card-shadow: rgba(0, 0, 0, 0.12);
  }
  html, body {
    margin: 0;
    padding: 0;
    width: 1200px;
    height: 800px;
    overflow: hidden;
    background: var(--backdrop);
    font-family: "Open Sans", Arial, sans-serif;
  }
  .canvas {
    position: relative;
    width: 1200px;
    height: 800px;
  }
  .card {
    position: absolute;
    top: 257px;
    width: 500px;
    height: 286px;
    background: var(--card-white);
    box-shadow: 0 6px 18px var(--card-shadow);
  }
  .card-front { left: 70px; }
  .card-back { left: 630px; }

  .brand-name {
    margin: 0;
    color: var(--brand-blue);
    font-weight: 400;
    line-height: 1;
    white-space: nowrap;
  }
  .card-front .brand-name {
    position: absolute;
    left: 50%;
    top: 50%;
    transform: translate(-50%, -50%);
    font-size: 56px;
  }
  .card-back .brand-name {
    position: absolute;
    left: 34px;
    top: 34px;
    font-size: 30px;
  }

  .holder {
    position: absolute;
    left: 40px;
    top: 168px;
  }
  .holder-name {
    color: var(--brand-blue);
    font-size: 13px;
    margin: 0;
  }
  .holder-title {
    color: var(--brand-green);
    font-size: 11px;
    margin: 1px 0 0;
  }

  .contact {
    position: absolute;
    left: 262px;
    top: 126px;
    margin: 0;
    padding: 0;
    list-style: none;
    color: var(--brand-blue);
    font-size: 12.5px;
    line-height: 19px;
    white-space: nowrap;
  }
  .contact-label { color: var(--brand-green); }
</style>
</head>
<body>
<main class="canvas">
  <section class="card card-front" aria-label="Business card front">
    <p class="brand-name">torvik</p>
  </section>

  <section class="card card-back" aria-label="Business card back">
    <p class="brand-name">torvik</p>

    <div class="holder">
      <p class="holder-name">Daniel Hartono</p>
      <p class="holder-title">President</p>
    </div>

    <ul class="contact">
      <li>Torvik Enterprises Corp.</li>
      <li>2418 W Alder St. Fairview CA 90512</li>
      <li><span class="contact-label">P</span> : 555 214 3870</li>
      <li><span class="contact-label">F</span> : 555 214 3871</li>
      <li><span class="contact-label">C</span> : 555 308 9142</li>
      <li><span class="contact-label">W</span> : www.torvikeats.com</li>
      <li><span class="contact-label">E</span> : Daniel@torvikeats.com</li>
    </ul>
  </section>
</main>
</body>
</html>
```